price list for web and print- sending to inquiring clients and use as promo material

Hello
I need a graphic design for my photography price list/s. I am a people photographer. The first of 6 price sheets will be for head shots- I would like a price sheet that captures the prospective clients' attention. The info and visual should be compelling and easy to digest. It should be simple yet interesting. I will provide you with some pictures but you do not have to include them. I have a studio indoors and outdoors also working on location. This design should be for email and print. The picture of "denise" is me and I use that on all my profiles. I like the fonts in the logo but it is too boxy and rigid

Target Market(s)

repeat client, word of mouth referrals, new people but aquaintances of others that might know me

Industry/Entity Type

Graphic Design

Font styles to use
Serif
Sans Serif
Script

Requirements
Must have
• prices and maybe some words about my services that I sent in... Please tie it together as best as possible..
Nice to have
• Loosen up my logo.. it is in a box.....contemporary design but not something that would not fit in with corporate.. I like this headline
• "Create a great first impression with your professional headshots"
• I sent in other copy and my logo(sent in the picture drop box)

```html
<!DOCTYPE html>
<html lang="en">
<head>
<meta charset="utf-8">
<title>Denise M. Harlow Photography – Headshot Price List</title>
<link rel="stylesheet" href="https://fonts.googleapis.com/css2?family=Open+Sans:ital,wght@0,400;0,600;0,700;1,400&family=Tinos:wght@400&family=Pinyon+Script&display=swap">
<style>
  :root {
    --paper: #f8f1ea;
    --ink: #1b1b1b;
    --coral: #f5877a;
    --coral-soft: #f7a89e;
    --photo: #121212;
    --frame: #ffffff;
    --dots: #ef9a91;
  }
  * { margin: 0; padding: 0; box-sizing: border-box; }
  html, body { width: 927px; height: 1200px; overflow: hidden; }
  body { background: var(--paper); color: var(--ink); font-family: "Tinos", serif; }
  .sheet { position: relative; width: 927px; height: 1200px; }
  .abs { position: absolute; }

  .quote-box { left: 68px; top: 72px; width: 266px; height: 134px; border: 1.5px dotted var(--dots); padding: 14px 0 0 40px; }
  .quote-text { font-family: "Open Sans", sans-serif; font-size: 21px; line-height: 27px; letter-spacing: 0.3px; }
  .quote-sign { font-family: "Pinyon Script", cursive; font-size: 22px; margin-top: 2px; margin-left: 0; }

  .brand { left: 376px; top: 112px; width: 204px; text-align: center; font-family: "Open Sans", sans-serif; font-weight: 400; font-size: 19px; line-height: 26px; letter-spacing: 1px; color: var(--ink); }

  .contact { left: 618px; top: 79px; font-family: "Open Sans", sans-serif; font-size: 15px; line-height: 21.6px; letter-spacing: 0.3px; font-style: normal; }

  .photo-stack { left: 56px; top: 208px; width: 360px; height: 300px; }

  .section-title { font-family: "Open Sans", sans-serif; font-weight: 700; letter-spacing: 3px; text-align: center; width: 300px; }
  .section-body { font-size: 17px; line-height: 26px; }

  .packages-title { left: 571px; top: 234px; font-family: "Open Sans", sans-serif; font-size: 29px; font-weight: 400; }
  .packages-title b { font-weight: 700; }
  .pkg-name { font-family: "Open Sans", sans-serif; font-weight: 700; font-size: 21px; }
  .pkg-sub { font-family: "Open Sans", sans-serif; font-style: italic; font-size: 21px; }
  .pkg-price { font-family: "Open Sans", sans-serif; font-size: 29px; text-align: right; width: 120px; }
  .pkg-list { list-style: none; font-size: 17px; line-height: 21.8px; }
  .setup { font-family: "Open Sans", sans-serif; font-size: 10px; }
  .footnote { left: 532px; top: 1043px; font-size: 13.5px; line-height: 18px; }

  .stamp { width: 74px; height: 56px; border: 1px solid var(--coral-soft); background: #fdf8f5; border-radius: 4px; transform: rotate(-28deg); font-family: "Pinyon Script", cursive; font-size: 17px; line-height: 18px; text-align: center; padding-top: 9px; }

  .tagline { left: 0; top: 1096px; width: 927px; text-align: center; font-family: "Pinyon Script", cursive; font-size: 27px; }
</style>
</head>
<body>
<main class="sheet">

  <section class="quote-box abs">
    <p class="quote-text">“MEMORIES ARE<br>WHAT WE CHERISH<br>MOST”</p>
    <p class="quote-sign">~ Denise M. Harlow</p>
  </section>

  <div class="brand abs">Denise M. Harlow<br>PHOTOGRAPHY</div>

  <address class="contact abs">
    1840 Linden Crest Drive<br>
    Atlanta, GA 30318<br>
    (404) 555-0142<br>
    (404) 555-0187 (cell)<br>
    dmhphoto@examplemail.com<br>
    www.dmhstudio.com
  </address>

  <svg class="photo-stack abs" viewBox="0 0 360 300" width="360" height="300">
    <g transform="rotate(-6 180 150)">
      <rect x="30" y="40" width="300" height="220" fill="var(--frame)"/>
      <rect x="38" y="48" width="284" height="204" fill="var(--photo)"/>
    </g>
    <g transform="rotate(5 190 150)">
      <rect x="40" y="30" width="300" height="230" fill="var(--frame)"/>
      <rect x="48" y="38" width="284" height="214" fill="var(--photo)"/>
    </g>
    <rect x="24" y="40" width="304" height="226" fill="var(--frame)"/>
    <rect x="32" y="48" width="288" height="210" fill="var(--photo)" role="img" aria-label="Portrait photograph of Denise"/>
    <polygon points="76,208 260,208 238,256 260,304 76,304 98,256" fill="var(--coral)"/>
    <text x="168" y="274" text-anchor="middle" font-family="Pinyon Script, cursive" font-size="46" fill="#ffffff">Denise</text>
  </svg>

  <h2 class="section-title abs" style="left:82px;top:528px;font-size:24px">EXPERIENCE</h2>
  <p class="section-body abs" style="left:88px;top:583px">Denise is an accomplished professional<br>photographer who has helped thousands<br>of clients. She is an expert at helping you<br>look confident and approachable.</p>

  <h2 class="section-title abs" style="left:66px;top:714px;font-size:26px;line-height:36px">24 HOUR<br>TURN AROUND</h2>
  <p class="section-body abs" style="left:81px;top:802px;line-height:21.8px">Your time is valuable. Denise can complete<br>the photoshoot in just 30 minutes. (Or as<br>long as you want.) Our process is designed to<br>save you time.</p>

  <h2 class="section-title abs" style="left:74px;top:914px;font-size:24px">ENJOYABLE</h2>
  <p class="section-body abs" style="left:88px;top:962px;line-height:21.8px">You can look forward to an<br>enjoyable photo session with Denise’s<br>professional guidance. Denise helps<br>make the experience fun.</p>

  <h1 class="packages-title abs"><b>Popular</b> Packages</h1>

  <div class="pkg-name abs" style="left:571px;top:281px">Entry Package</div>
  <div class="pkg-price abs" style="left:730px;top:278px">$175</div>
  <div class="pkg-sub abs" style="left:571px;top:309px">Quick and Simple</div>
  <ul class="pkg-list abs" style="left:606px;top:349px">
    <li>One pose</li><li>One wardrobe</li><li>One selected image retouched</li><li>(Additional images $75 each)</li>
  </ul>

  <div class="stamp abs" style="left:482px;top:456px">Most<br>Popular</div>
  <div class="pkg-name abs" style="left:571px;top:471px">2 Pose Package</div>
  <div class="pkg-price abs" style="left:730px;top:466px">$175</div>
  <ul class="pkg-list abs" style="left:606px;top:508px">
    <li>Two poses</li><li>Two wardrobe changes</li><li>Two selected images retouched</li><li>One or two background changes</li><li>(Additional images $75 each)</li>
  </ul>

  <div class="stamp abs" style="left:486px;top:637px">Most<br>Popular</div>
  <div class="pkg-name abs" style="left:570px;top:633px">Premier Package</div>
  <div class="pkg-sub abs" style="left:570px;top:663px">Get It All</div>
  <div class="pkg-price abs" style="left:733px;top:658px">$525</div>
  <ul class="pkg-list abs" style="left:606px;top:699px">
    <li>Four poses</li><li>3-4 wardrobe changes</li><li>4 selected images retouched</li><li>2-3 background changes</li><li>(Additional images $75 each)</li><li>(Optional outdoor studio)</li>
  </ul>

  <div class="pkg-name abs" style="left:570px;top:862px">Choice Location</div>
  <div class="pkg-price abs" style="left:740px;top:855px">$250</div>
  <div class="setup abs" style="left:795px;top:901px">set up charge</div>
  <ul class="pkg-list abs" style="left:606px;top:903px">
    <li>Minmum 5 people</li><li>One selected image retouched</li><li>5-10 people - $150 each</li><li>11-20 people - $100 each</li><li>20+ people - $75 each</li><li>(Additional images $50 each)</li>
  </ul>
  <p class="footnote abs">If possible, we like 30 minute appointments for each<br>person so they can view their images on the computer.</p>

  <p class="tagline abs">"Create a great first impression with your professional headshots"</p>

</main>
</body>
</html>
```